CD Album Cover design for band's first album.

We are an Australian rock band called The Copper Loom. We are seeking designs for our first album cover. The album will be self titled 'The Copper Loom'.

Samples in the upload files are 2 songs and artworks we have used for merchandise; t-shirt and stubby holders. Please message me if you'd like to listen to more of the album for better idea references.
Updates

Greetings! We have updated the briefing notes. Most important update in the "must not have" section: Please do not use the current graphics in the sample uploads. We use these for merchandise and looking for fresh ideas. Your art should not contain the words "drifting past noon" or "harbour". Thank you for your submissions to date!

Target Market(s)

International audience. The artwork will be displayed for our online presence and streaming subscriptions.

Industry/Entity Type

Entertainment Industry

Colors

Designer to choose colors to be used in the design.

Requirements
Must have
• Your cover art must be:
• · Either 3000 x 3000 pixels (preferred) or 1400 x 1400 pixels
• · PNG, GIF, JPG, or JPEG file type
• · 72 - 300dpi (300dpi is the best)
• · Less than 25mb
• · RGB color scheme (not CMYK)
Should not have
• Please do not use the current graphics in the sample uploads. We use these for merchandise and are looking for fresh ideas.
• Your art should not contain the words "drifting past noon" or "harbour".

```html
<!DOCTYPE html>
<html lang="en">
<head>
<meta charset="utf-8">
<title>The Copper Loom – Album Cover</title>
<link rel="stylesheet" href="https://fonts.googleapis.com/css2?family=Montserrat:wght@400;700&display=swap">
<style>
  :root {
    --backdrop: #eceff0;
    --frame-white: #f4f4f2;
    --frame-edge: #d8d8d6;
    --photo-black: #080809;
    --photo-dark: #141314;
    --photo-mid: #2e2a2b;
    --photo-light: #4a4547;
    --photo-rust: #5a2a28;
    --photo-teal: #1c2a2c;
    --banner-white: #f7f6f2;
    --banner-ink: #2a1f1d;
    --title-white: #ffffff;
  }
  * { box-sizing: border-box; margin: 0; padding: 0; }
  html, body {
    width: 1200px;
    height: 750px;
    overflow: hidden;
    background: var(--backdrop);
  }
  .canvas {
    position: relative;
    width: 1200px;
    height: 750px;
  }
  .album-cover {
    position: absolute;
    left: 320px;
    top: 95px;
    width: 560px;
    height: 560px;
    background: var(--frame-white);
    border: 1px solid var(--frame-edge);
    box-shadow: 0 2px 6px rgba(0, 0, 0, 0.12);
  }
  .cover-photo {
    position: absolute;
    left: 14px;
    top: 12px;
    right: 14px;
    bottom: 18px;
    background:
      radial-gradient(ellipse 38% 30% at 50% 40%, rgba(8, 8, 9, 0.85) 0%, rgba(8, 8, 9, 0) 100%),
      radial-gradient(ellipse 62% 52% at 50% 40%, rgba(90, 42, 40, 0) 40%, rgba(90, 42, 40, 0.45) 62%, rgba(90, 42, 40, 0) 78%),
      radial-gradient(ellipse 70% 40% at 50% 8%, rgba(74, 69, 71, 0.9) 0%, rgba(74, 69, 71, 0) 100%),
      radial-gradient(ellipse 40% 50% at 20% 30%, rgba(28, 42, 44, 0.7) 0%, rgba(28, 42, 44, 0) 100%),
      radial-gradient(ellipse 40% 50% at 82% 34%, rgba(46, 42, 43, 0.8) 0%, rgba(46, 42, 43, 0) 100%),
      linear-gradient(180deg, var(--photo-mid) 0%, var(--photo-dark) 55%, var(--photo-black) 100%);
  }
  .name-banner {
    position: absolute;
    left: 50%;
    top: 38px;
    transform: translateX(-50%);
    width: 310px;
    height: 58px;
  }
  .name-banner svg {
    position: absolute;
    inset: 0;
  }
  .banner-name {
    position: absolute;
    inset: 0;
    display: flex;
    align-items: center;
    justify-content: center;
    padding-top: 2px;
    font-family: 'Montserrat', sans-serif;
    font-weight: 400;
    font-size: 20px;
    letter-spacing: 2px;
    color: var(--banner-ink);
    text-transform: uppercase;
  }
  .album-title {
    position: absolute;
    left: 0;
    right: 0;
    bottom: 48px;
    text-align: center;
    font-family: 'Montserrat', sans-serif;
    font-weight: 400;
    font-size: 24px;
    letter-spacing: 0.5px;
    color: var(--title-white);
    text-transform: uppercase;
  }
  .album-title strong { font-weight: 700; }
</style>
</head>
<body>
  <main class="canvas">
    <section class="album-cover">
      <div class="cover-photo" role="img" aria-label="Dark photograph looking up into a domed glass ceiling with radiating rust-red iron ribs"></div>

      <div class="name-banner">
        <svg viewBox="0 0 310 58" width="310" height="58" aria-hidden="true">
          <path d="M4 16 Q155 -2 306 16 L306 48 Q155 32 4 48 Z"
                fill="var(--banner-white)" stroke="var(--banner-ink)" stroke-width="2"/>
        </svg>
        <span class="banner-name">The Copper Loom</span>
      </div>

      <h1 class="album-title">The <strong>Copper</strong> Loom</h1>
    </section>
  </main>
</body>
</html>
```